Email Signature Design

Please design an email signature, the below is an example of our current design;
___

CARRODY ESTATE HOLDINGS PTY LTD
BENEDICT HARLOWE
Licensed Strata and Community Manager

143 Tallowood Street,
KELDARRA NSW 2093

P: 02.9473.6820 F: 9536.2048
Website: www.carrodyestate.com.au

This e-mail message and accompanying data may contain information that is confidential and private. If you are not the intended recipient, the use, dissemination, distribution or copying of this message or data is prohibited.

If you have received this e-mail in error please notify us immediately and delete all material pertaining to this e-mail. strata@carrodyestate.com.au

___

We would like to incorporate our logo and company colours, you can view the colours and feel of image at www.carrodyestate.com.au

Industry/Entity Type

It Company

Requirements
Must have
• use of logo and company colours (image)

```html
<!DOCTYPE html>
<html lang="en">
<head>
<meta charset="utf-8">
<title>Carrody Estate Holdings – Email Signature</title>
<link href="https://fonts.googleapis.com/css2?family=Arimo:wght@400;700&display=swap" rel="stylesheet">
<style>
  :root {
    --olive: #857d3c;
    --grey: #6b6b6d;
    --ink: #1f1f1f;
    --body: #444444;
    --paper: #ffffff;
  }
  html, body {
    margin: 0;
    padding: 0;
    overflow: hidden;
    background: var(--paper);
  }
  .signature {
    position: relative;
    width: 1200px;
    height: 333px;
    overflow: hidden;
    background: var(--paper);
    font-family: "Arimo", Arial, sans-serif;
    color: var(--ink);
  }
  .brand-mark {
    position: absolute;
    left: 113px;
    top: 62px;
    width: 90px;
    height: 90px;
    background: var(--olive);
  }
  .brand-name {
    position: absolute;
    left: 113px;
    top: 162px;
    margin: 0;
    font-size: 19px;
    font-weight: 700;
    letter-spacing: 0.2px;
    color: var(--olive);
    white-space: nowrap;
  }
  .brand-tagline {
    position: absolute;
    left: 113px;
    top: 183px;
    margin: 0;
    font-size: 13px;
    letter-spacing: 0.6px;
    color: var(--grey);
    white-space: nowrap;
  }
  .divider {
    position: absolute;
    left: 446px;
    top: 58px;
    width: 3px;
    height: 139px;
    background: var(--olive);
  }
  .contact {
    position: absolute;
    left: 523px;
    top: 56px;
    font-size: 16px;
  }
  .contact p { margin: 0; white-space: nowrap; }
  .contact-name {
    font-weight: 700;
    color: var(--olive);
    font-size: 16px;
    height: 27px;
  }
  .contact-title { height: 29px; }
  .contact-address { height: 36px; }
  .contact-row {
    display: flex;
    align-items: center;
    gap: 6px;
    height: 29px;
    font-size: 17px;
  }
  .badge {
    display: inline-flex;
    align-items: center;
    justify-content: center;
    width: 19px;
    height: 19px;
    border-radius: 50%;
    background: var(--olive);
    color: var(--paper);
    font-size: 12px;
  }
  .badge-gap { margin-left: 10px; }
  .disclaimer {
    position: absolute;
    left: 108px;
    top: 210px;
    width: 1000px;
    font-size: 14.4px;
    line-height: 22px;
    color: var(--body);
  }
  .disclaimer p { margin: 0 0 8px; }
</style>
</head>
<body>
  <div class="signature">
    <div class="brand-mark" aria-hidden="true"></div>
    <p class="brand-name">CARRODY ESTATE HOLDINGS</p>
    <p class="brand-tagline">STRATA MANAGEMENT SERVICES</p>

    <div class="divider" aria-hidden="true"></div>

    <div class="contact">
      <p class="contact-name">BENEDICT HARLOWE</p>
      <p class="contact-title">Licensed Strata and Community Manager</p>
      <p class="contact-address">143 Tallowood Street, KELDARRA NSW 2093</p>
      <p class="contact-row">
        <span class="badge">P</span><span>02.9473.6820</span>
        <span class="badge badge-gap">F</span><span>9536.2048</span>
      </p>
      <p class="contact-row">
        <span class="badge">W</span><span>www.carrodyestate.com.au</span>
      </p>
    </div>

    <div class="disclaimer">
      <p>This e-mail message and accompanying data may contain information that is confidential and private. If you are not the intended recipient, the use, dissemination, distribution or copying of this message or data is prohibited.</p>
      <p>If you have received this e-mail in error please notify us immediately and delete all material pertaining to this e-mail. strata@carrodyestate.com.au</p>
    </div>
  </div>
</body>
</html>
```